Real Estate Website

I have a very old website that was built almost 20 years ago. We are rebuilding it and need a fresh new design for it please.
The existing website is https://northpeakhomes.example

This is for a real estate company that is selling real estate in Hokkaido, Japan (known for it's skiing and snow tourism) and is all in english as it targets westerners looking to buy holiday homes or investment properties.
Updates

Hi everyone.

Sorry this has taken so long to get back to you. My client has taken a long time to get back to me after the Christmas break.

Unfortunately they did not want to go ahead with any of the designs submitted as they said they look too much like business sales websites instead of residential and commercial sales. An example of what they lik is https://www.velmorproperty.example/
They don't want it to look at all like their business sales website (https://www.ranscombebusinesssales.example/) and have said:

• keep Ra NSCOMBE GROUP logo and color scheme the same
• Give freedom to the designers, on how what to execute what the company does.
-Commercial/Industrial
-Residential

Make them separate as there’s a different audience of clients for commercial & residential are very different.

I will provide some content and headings which you have the freedom to play around and coordinate. What I provide below are only suggestions, please feel free to be use your ideas and be innovative.

Residential listings - would like the listing to shows Features on details page.
Commercial listings – must display “building area” on the front page
HEADINGS ON TOP OF PAGE -TABS:
HOME - This MUST show on the tab
COMMERCIAL/INDUSTRIAL - This MUST show on the tab
RESIDENTIAL - This MUST show on the tab
BUSINESS SALES (this to link straight to my RANSCOMBE BUSINESS SALES & VUALUATIONS website - This MUST show on the tab
ABOUT US
BLOGS/videos- I want my team to be able to load all the videos, eg when they do videos for auctions, developments etc -– optional, if not enough space, show it on the bottom of the website ( you could also add under ABOUT US tab)
CONTACT US

Maybe show this on the home screen heading:
Specialists in Commercial/ Industrial Property,
Trusted in Residential Property

Theme:
“Maximising returns, protecting investments, expert property advisory”
Work With Us

The Information below is not in any particle order:

Book an Appraisal
Discover the Real Value of Your Property
At Ranscombe Group, we don’t just provide standard appraisals — we deliver strategic, insight-driven reports that uncover the true drivers of your property’s worth. Whether it’s commercial, industrial, or residential, our expertise ensures you see the full picture.
From market trends and rental potential to investment performance and future growth opportunities, our tailored reports give you clarity, confidence, and actionable insights.
Book a confidential consultation today and gain the expert guidance you need to maximise returns and make smarter property decisions.

What We Do
What We Do – Property Management, Sales & Leasing
At Ranscombe Group, we specialise in guiding property owners, investors, and landlords through the complexities of managing, selling, leasing, and valuing assets. Our mission is clear: to deliver clarity, confidence, and measurable results at every stage of your property journey.
We go beyond standardised reports. Our strategic, insight-driven valuations and management solutions uncover the true drivers of your property’s performance. From tailored marketing campaigns and compelling listings to confidential negotiations and introductions, we ensure your asset attracts the right tenants, buyers, or investors.
When the future of your investment is on the line, you need more than a property manager or agent — you need a partner who delivers certainty, strategy, and results. At Ranscombe Group, we don’t just manage, lease, or sell properties; we maximise value, income, and long-term growth.
Contact us today for a confidential consultation and discover how Ranscombe Group can help you achieve the strongest outcomes for your property portfolio.

Who We Are
At Ranscombe Group, we are recognised as a trusted authority in commercial and residential property management, sales, and leasing. Property owners, investors, and developers turn to us for our proven expertise, discretion, and consistent results.
Our mission is to set the standard for excellence in property services. Guided by innovation, integrity, and strategic execution, we deliver outcomes that protect assets, maximise returns, and create enduring value for our clients.
Whether your goal is to manage your investment, increase rental income, lease to the right tenants, or achieve a successful sale, we provide clarity, confidence, and tailored solutions at every stage of the journey.
Let’s begin the conversation today — and explore how Ranscombe Group can help you achieve the strongest results for your property portfolio.

Commercial & Industrial Property Management & Leasing

At Ranscombe Group, we are recognised as a leading authority in the management and leasing of premium commercial and industrial assets. Trusted by investors, landlords, and developers, our portfolio spans medical centres, healthcare facilities, allied health clinics, global franchise brands such as BWQ and The Marmalade Pantry, high‑end retail outlets, and large‑scale industrial and manufacturing properties.
We deliver strategic, results‑driven property solutions that combine market intelligence, operational excellence, and meticulous attention to detail. Our approach is designed to maximise returns, minimise vacancies, and safeguard long‑term asset performance.

Our Services
• Strategic Marketing & Leasing – Positioning your property to attract premium tenants through targeted, multi‑channel campaigns.
• Tenant & Lease Administration – Precision management of agreements, renewals, compliance, and documentation.
• Revenue Optimisation – Proactive rent collection, vacancy minimisation, and lease structuring to elevate asset value.
• Maintenance & Property Upkeep – Access to vetted, high‑quality trades for repairs and preventative care, ensuring assets remain in peak condition.
• Regulatory Compliance & Essential Services – Full oversight of statutory obligations and essential service measures, protecting both compliance and reputation.
Why Choose us
• Sector Expertise – Deep knowledge across medical, healthcare, franchise, retail, and industrial sectors, enabling tailored strategies for each asset class.
• Proactive Asset Management – Beyond operations, we actively enhance value, mitigate risk, and secure the right tenants.
• Bespoke Solutions – Every property is unique. We craft customised management and leasing strategies aligned with your objectives and market conditions.
• Professional Excellence – Integrity, precision, and industry‑leading best practices deliver measurable results and peace of mind for discerning property owners.
With Ranscombe Group, your commercial and industrial assets are managed with authority, insight, and excellence — ensuring performance that meets the expectations of high‑end investors and developers.

```html
<!DOCTYPE html>
<html lang="en">
<head>
<meta charset="utf-8">
<title>North Peak Homes – Property in Hokkaido</title>
<link rel="stylesheet" href="https://fonts.googleapis.com/css2?family=Libre+Baskerville:wght@400;700&family=Roboto:wght@400;500;700&display=swap">
<style>
:root{
  --red:#c8102e;
  --red-dark:#8e0d1e;
  --ink:#222;
  --text:#3a3a3a;
  --pink:#f6e6ea;
  --grey-btn:#3d3d3d;
  --line:#cfcfcf;
  --black:#000;
  --white:#fff;
}
*{box-sizing:border-box;margin:0;padding:0}
html,body{width:1200px;height:4491px;overflow:hidden;background:var(--white)}
body{font-family:"Roboto",Arial,sans-serif;color:var(--text)}
.page{position:relative;width:1200px;height:4491px;overflow:hidden}
.abs{position:absolute}
.serif{font-family:"Libre Baskerville",Georgia,serif}

/* header */
.site-header{left:0;top:0;width:1200px;height:101px;background:var(--white)}
.brand{left:143px;top:18px;display:flex;align-items:center;gap:12px}
.brand-mark{width:40px;height:40px;border-radius:50%;background:var(--red)}
.brand-name{font-family:"Libre Baskerville",Georgia,serif;font-weight:700;font-size:22px;line-height:1.05;color:var(--ink);letter-spacing:1px}
.call{left:694px;top:28px;display:flex;align-items:center;gap:12px}
.call-icon{width:28px;height:28px;border-radius:50%;background:var(--red);display:flex;align-items:center;justify-content:center}
.call small{display:block;color:var(--red);font-size:13px;font-weight:500}
.call strong{display:block;font-size:19px;font-weight:500;color:var(--ink)}
.social{display:flex;gap:10px}
.social span{width:34px;height:34px;border-radius:50%;background:var(--black);display:block}
.social span.alt{background:var(--white);border:2px solid var(--red)}
.header-social{left:934px;top:33px}

.main-nav{left:0;top:101px;width:1200px;height:47px;background:var(--red)}
.main-nav ul{list-style:none;display:flex;justify-content:center;gap:24px;position:absolute;left:0;top:12px;width:1200px}
.main-nav li{color:var(--white);font-size:13px;font-weight:500;line-height:23px;text-transform:uppercase;white-space:nowrap}
.main-nav li.active{background:#2d2d2d;padding:0 11px}

/* hero */
.hero{left:0;top:148px;width:1200px;height:680px;background:linear-gradient(180deg,#4a4668 0%,#b9714f 22%,#e4a063 33%,#6c5a5d 45%,#3d5370 60%,#2b3c52 80%,#3a3440 100%)}
.hero-title{left:143px;top:308px;font-size:47px;font-weight:700;color:var(--white);letter-spacing:1px;text-shadow:0 2px 6px rgba(0,0,0,.4)}
.btn{position:absolute;display:flex;align-items:center;justify-content:center;font-size:13px;font-weight:700;text-transform:uppercase;border-radius:4px;white-space:nowrap}
.btn-red{background:var(--red);color:var(--white)}
.btn-outline-white{border:2px solid var(--white);color:var(--white)}
.btn-outline-red{border:2px solid var(--red);color:var(--red);background:var(--white)}
.btn-dark{background:var(--grey-btn);color:var(--white)}
.btn-white{background:var(--white);color:var(--red)}
.slider-dots{left:1114px;top:317px;display:flex;flex-direction:column;gap:14px}
.slider-dots i{width:11px;height:11px;border-radius:50%;background:var(--white);display:block}
.slider-dots i.off{background:transparent;border:2px solid var(--white)}

/* search */
.search{left:192px;top:738px;width:816px;height:160px;background:var(--white);border-radius:12px;box-shadow:0 8px 24px rgba(0,0,0,.15)}
.search h2{position:absolute;left:63px;top:26px;font-size:22px;font-weight:700;color:var(--ink)}
.select{position:absolute;top:73px;width:163px;height:42px;border:2px solid #d6d6d6;border-radius:3px;font-size:13.5px;color:#333;padding:0 20px;display:flex;align-items:center;justify-content:space-between}
.select::after{content:"";border:5px solid transparent;border-top-color:#333;margin-top:5px}

/* welcome */
.welcome-bg{left:0;top:1220px;width:1200px;height:680px;background:linear-gradient(180deg,#fff 0%,rgba(255,255,255,.7) 30%,#b49485 55%,#7a5a43 72%,#5b4b3e 100%)}
.welcome-title{left:0;top:1008px;width:1200px;text-align:center}
.welcome-title .l1{font-size:46px;font-weight:700;color:var(--ink);display:block}
.welcome-title .l2{font-size:42px;font-weight:400;color:var(--red);display:block;margin-top:10px;letter-spacing:1px}
.intro{top:1163px;width:433px;font-size:15px;line-height:28.5px;text-align:justify;color:var(--text)}

.section-title{left:0;width:1200px;text-align:center;font-size:46px;font-weight:700;color:var(--ink)}
.section-title em{font-style:normal;font-weight:400;color:var(--red)}

/* featured */
.pink-band{left:0;top:1650px;width:1200px;height:630px}
.snow-bg{left:0;top:2274px;width:1200px;height:530px;background:linear-gradient(180deg,#fff 0%,#e6e7ec 40%,#c9cbd3 75%,#aeb1bb 100%)}
.card{top:2063px;width:290px;height:445px;background:var(--white);box-shadow:0 6px 18px rgba(0,0,0,.1)}
.card.current{border-bottom:5px solid var(--red)}
.card-photo{position:absolute;left:0;top:0;width:290px;height:211px}
.card h3{position:absolute;left:35px;top:240px;font-size:16px;font-weight:700;color:var(--ink);white-space:nowrap}
.card .meta{position:absolute;left:35px;top:272px;display:flex;gap:18px;font-size:12.5px;color:#555}
.card .meta span{display:flex;align-items:center;gap:7px}
.card .meta i{width:13px;height:9px;background:var(--red);display:block;border-radius:1px}
.card p{position:absolute;left:35px;top:298px;width:220px;font-size:13.5px;line-height:22px;color:#444}
.card .btn{left:35px;top:377px;width:142px;height:38px;font-size:12px}

/* selling */
.panel{top:2803px;height:480px;width:616px}
.panel-left{left:0;background:linear-gradient(135deg,#3c3c3c,#2a2a2a 60%,#4a4a4a)}
.panel-right{left:616px;width:584px;background:linear-gradient(135deg,#a0101e,#7a0c17 55%,#c8102e)}
.panel h3{position:absolute;top:115px;font-size:27px;font-weight:500;color:var(--white)}
.panel p{position:absolute;top:160px;font-size:15px;line-height:28.5px;color:var(--white);text-align:justify}
.panel .btn{top:331px;height:38px;font-size:12px}

/* contact */
.contact-bg{left:0;top:3282px;width:1200px;height:790px;background:linear-gradient(180deg,#d8c9c8 0%,#efe6e5 22%,#fff 45%,#fff 100%)}
.field{position:absolute;border:2px solid #d3d3d3;background:var(--white);font-size:15px;color:#555;padding:0 20px;display:flex;align-items:center}
.city-art{left:0;top:3790px;width:1200px;height:280px;background:linear-gradient(180deg,rgba(255,255,255,0) 0%,#f1f1f3 50%,#e4e4e8 100%)}

/* footer */
.footer-contact{left:0;top:4190px;width:1200px;display:flex;justify-content:center;align-items:center;gap:30px;color:var(--white);font-size:20px}
.footer-contact .item{display:flex;align-items:center;gap:14px;white-space:nowrap}
.footer-contact .dot{width:32px;height:32px;border-radius:50%;background:var(--white)}
.footer-contact .dot.red{background:var(--red)}
.footer-contact .sep{width:1px;height:44px;background:#444}
.footer-rule{left:143px;top:4268px;width:914px;height:1px;background:#262626}
.footer-nav{left:0;top:4304px;width:1200px;display:flex;justify-content:center;gap:30px;list-style:none}
.footer-nav li{color:var(--white);font-size:13.5px;font-weight:700;text-transform:uppercase;white-space:nowrap}
.copyright{left:0;top:4362px;width:1200px;text-align:center;color:var(--white);font-size:14px}
.footer-social{left:541px;top:4415px}
.footer-social span{background:var(--white)}
.footer-social span.alt{background:var(--black);border-color:var(--red)}
</style>
</head>
<body>
<div class="page">

  <header class="site-header abs">
    <div class="brand abs">
      <span class="brand-mark"></span>
      <span class="brand-name">NORTH PEAK<br>HOMES</span>
    </div>
    <div class="call abs">
      <span class="call-icon">
        <svg width="14" height="14" viewBox="0 0 24 24"><path fill="#fff" d="M6.6 10.8a15 15 0 0 0 6.6 6.6l2.2-2.2c.3-.3.7-.4 1-.2 1.1.4 2.3.6 3.6.6.6 0 1 .4 1 1V20c0 .6-.4 1-1 1A17 17 0 0 1 3 4c0-.6.4-1 1-1h3.5c.6 0 1 .4 1 1 0 1.3.2 2.5.6 3.6.1.3 0 .7-.2 1z"/></svg>
      </span>
      <div><small>CALL US</small><strong>+81 123 45 6789</strong></div>
    </div>
    <div class="social header-social abs" aria-label="Social links"><span></span><span class="alt"></span><span></span></div>
  </header>

  <nav class="main-nav abs">
    <ul>
      <li class="active">Home</li><li>Commercial/Industrial</li><li>Residential</li><li>Business Sales</li><li>About Us</li><li>Blogs/Videos</li><li>Selling</li><li>Contact Us</li>
    </ul>
  </nav>

  <section class="hero abs" role="img" aria-label="Photo of a snow-capped mountain at sunset above a lake town in autumn"></section>
  <svg class="abs" style="left:0;top:650px" width="1200" height="180" viewBox="0 0 1200 180">
    <path d="M0 117 C 120 150 190 175 240 180 L1200 180 L1200 35 C 1000 20 800 25 650 90 C 560 130 420 140 240 150 C 150 150 70 135 0 117Z" fill="#fff"/>
    <path d="M650 90 C 800 25 1000 20 1200 35" fill="none" stroke="#c8102e" stroke-width="8"/>
    <path d="M0 117 C 70 135 130 150 200 160" fill="none" stroke="#c8102e" stroke-width="5"/>
  </svg>
  <h1 class="hero-title abs serif">NORTH PEAK HOMES</h1>
  <div class="btn btn-red" style="left:145px;top:415px;width:256px;height:56px">Most Featured Properties</div>
  <div class="btn btn-outline-white" style="left:417px;top:415px;width:256px;height:56px">Newly Listed Properties</div>
  <div class="slider-dots abs"><i></i><i></i><i></i><i class="off"></i></div>

  <form class="search abs">
    <h2 class="serif">PROPERTY SEARCH</h2>
    <div class="select" style="left:63px">Bedrooms</div>
    <div class="select" style="left:239px">Bathrooms</div>
    <div class="select" style="left:413px">Property type</div>
    <div class="select" style="left:588px">Location</div>
    <div class="btn btn-red" style="left:614px;top:139px;width:158px;height:39px;font-size:12px">Find Properties</div>
  </form>

  <div class="welcome-bg abs" role="img" aria-label="Photo of an autumn mountainside with a ski lift station"></div>
  <div class="welcome-title abs serif"><span class="l1">WELCOME TO</span><span class="l2">NORTH PEAK HOMES</span></div>
  <p class="intro abs" style="left:143px">An investment in Hokkaido property offers tremendous potential for both lifestyle and financial returns. But, the market is complex and dynamic. To invest wisely you need advice on all the potential pitfalls.The North Peak Homes team is small and dedicated group of professionals focused on delivering the best outcome for our clients whilst never compromising our ethical standards. As a result, we have some very loyal and long-time clients whom we have assisted to buy and sell properties for more than 15 years.We are not developers, and indeed seldom sell on behalf of developers. We seldom invest in the market, although we have sold our own homes from time to time.</p>
  <p class="intro abs" style="left:624px">We have sold more than 400 properties since we opened our doors in the then infant Niseko market in 2003. 75% of our sales have never appeared on our website. Rather, they have resulted from clients approaching us with a wishlist, and NPH being able to find a suitable property and successfully negotiate a purchase. Our successful sales range in price from as low 3 million yen up to more than 3 billion yen. Many of our sales are not in the Niseko region, we have sold properties from many parts of Hokkaido.<br><br>Please contact us if you feel we can help you</p>
  <div class="btn btn-red" style="left:337px;top:1561px;width:254px;height:52px">Read More Info</div>
  <div class="btn btn-outline-red" style="left:607px;top:1561px;width:255px;height:52px">Recent Property Sales</div>

  <svg class="pink-band abs" width="1200" height="630" viewBox="0 0 1200 630">
    <path d="M0 160 C 120 230 280 250 420 190 C 560 120 620 50 780 30 C 950 10 1100 40 1200 40 L1200 630 L0 630Z" fill="#f6e6ea"/>
  </svg>
  <div class="snow-bg abs" role="img" aria-label="Faded photo of snowy mountain peaks"></div>

  <h2 class="section-title abs serif" style="top:1962px">FEATURED <em>PROPERTIES</em></h2>

  <article class="card abs" style="left:143px">
    <div class="card-photo" role="img" aria-label="Photo of a snow-covered timber chalet" style="background:linear-gradient(180deg,#9fb4cf,#e9edf2 55%,#3a3f4a 75%,#f1f3f6)"></div>
    <h3>SED UTPERSPICIATIS UNDE</h3>
    <div class="meta"><span><i></i>2 Bedrooms</span><span><i></i>2 Bathrooms</span></div>
    <p>Nemo enim ipsam voluptatem quia voluptas sit aspernatur aut odit aut fugitsed</p>
    <div class="btn btn-dark">Read More Info</div>
  </article>
  <article class="card current abs" style="left:455px">
    <div class="card-photo" role="img" aria-label="Photo of a traditional half-timbered house in snow" style="background:linear-gradient(180deg,#d9dde2,#eceef0 30%,#4a3a30 60%,#8a7a6c 80%,#f0f0f0)"></div>
    <h3>SED UTPERSPICIATIS UNDE</h3>
    <div class="meta"><span><i></i>2 Bedrooms</span><span><i></i>2 Bathrooms</span></div>
    <p>Nemo enim ipsam voluptatem quia voluptas sit aspernatur aut odit aut fugitsed</p>
    <div class="btn btn-dark">Read More Info</div>
  </article>
  <article class="card abs" style="left:766px">
    <div class="card-photo" role="img" aria-label="Photo of a red-roofed farmhouse beside a green wheat field" style="background:linear-gradient(180deg,#e8edf2,#c9d3dc 25%,#7b4b3c 42%,#6e8b3d 55%,#5a7a2e 100%)"></div>
    <h3>SED UTPERSPICIATIS UNDE</h3>
    <div class="meta"><span><i></i>2 Bedrooms</span><span><i></i>2 Bathrooms</span></div>
    <p>Nemo enim ipsam voluptatem quia voluptas sit aspernatur aut odit aut fugitsed</p>
    <div class="btn btn-dark">Read More Info</div>
  </article>
  <div class="btn btn-red" style="left:473px;top:2564px;width:254px;height:54px">View More Properties</div>

  <h2 class="section-title abs serif" style="top:2714px">SELLING <em>PROPERTIES</em></h2>

  <section class="panel panel-left abs" role="img" aria-label="Dark toned photo of a snowy ski town">
    <h3 style="left:146px">Marketing Strategies</h3>
    <p style="left:148px;width:368px">At North Peak Homes we understand that there is a lot more to selling your overseas home than simply placing a 'For Sale' sign in front of your property. Real estate is all about information exchange - at which we excel!</p>
    <div class="btn btn-red" style="left:148px;width:142px">Read More Info</div>
  </section>
  <section class="panel panel-right abs" role="img" aria-label="Red toned photo of a lakeside landscape">
    <h3 style="left:70px">Sale by Exclusive Agency</h3>
    <p style="left:72px;width:368px">Your property would be placed in our hands as exclusive agents for an agreed period of time. As your exclusive agent we are committed to actively marketing your property and to giving you all the feedback.</p>
    <div class="btn btn-white" style="left:72px;width:143px">Read More Info</div>
  </section>

  <div class="contact-bg abs" role="img" aria-label="Faded photo of a snow-capped mountain with red autumn leaves"></div>
  <h2 class="section-title abs serif" style="top:3385px">CONTACT <em>US</em></h2>
  <p class="abs" style="left:0;top:3460px;width:1200px;text-align:center;font-size:21px;color:#333">Please send us an email with your inquiry</p>
  <div class="field" style="left:235px;top:3532px;width:358px;height:50px">First Name</div>
  <div class="field" style="left:605px;top:3532px;width:359px;height:50px">Last Name</div>
  <div class="field" style="left:235px;top:3596px;width:358px;height:51px">Email address</div>
  <div class="field" style="left:605px;top:3596px;width:359px;height:51px">Phone Number</div>
  <div class="field" style="left:235px;top:3662px;width:729px;height:114px;align-items:flex-start;padding-top:16px">Message</div>
  <div class="city-art abs" role="img" aria-label="Line illustration of a city skyline with clouds"></div>
  <div class="btn btn-red" style="left:492px;top:3807px;width:216px;height:54px">Submit Message</div>

  <svg class="abs" style="left:0;top:3925px" width="1200" height="566" viewBox="0 0 1200 566">
    <path d="M0 140 C 300 140 440 110 580 55 C 720 10 950 5 1200 15 L1200 566 L0 566Z" fill="#000"/>
    <path d="M400 118 C 470 100 520 80 580 55 C 720 10 950 5 1200 15" fill="none" stroke="#c8102e" stroke-width="9"/>
  </svg>

  <footer>
    <div class="footer-contact abs">
      <div class="item"><span class="dot"></span>Email: info@northpeakhomes.example</div>
      <span class="sep"></span>
      <div class="item"><span class="dot red"></span>Call our office on <strong>+81 123 45 6789</strong></div>
    </div>
    <div class="footer-rule abs"></div>
    <ul class="footer-nav abs">
      <li>Home</li><li>Commercial/Industrial</li><li>Residential</li><li>Business Sales</li><li>About Us</li><li>Blogs/Videos</li><li>Selling</li><li>Contact Us</li>
    </ul>
    <p class="copyright abs">© 2026 North Peak Homes - All Rights Reserved &nbsp;/&nbsp; Terms of use &nbsp;/&nbsp; Privacy Policy</p>
    <div class="social footer-social abs" aria-label="Social links"><span></span><span class="alt"></span><span></span></div>
  </footer>

</div>
</body>
</html>
```